Selka Varon Photography

I need a website design for my photography business, I want something clean, elegant, Classy.. I like the colors, White, Black, Green/Blue, Pink, Brown, Lavender,, I have a lot added my Logo .... Additional Info... I need a Photography Website Design, with probably 6 Tabs, Home, About Me, Portfolio, Gallery, Investment, Contact.
Home Page should have my logo, Name & Address, Social Media Icons, and Pictures.
As long as the templates are made I have a hosting coming that will code it.
Portraits Photography, Senior Portraits, Newborn, Families, Events, Engagements, Wedding,
Business
5+ page

```html
<!DOCTYPE html>
<html lang="en">
<head>
<meta charset="utf-8">
<title>Selka Varon Photography — Home</title>
<link href="https://fonts.googleapis.com/css2?family=Jost:wght@300;400&display=swap" rel="stylesheet">
<style>
  :root {
    --bg: #000000;
    --text-soft: #a9a9a9;
    --text-mute: #8c8c8c;
    --text-bright: #ffffff;
    --rule: #3a3a3a;
    --rule-light: #7a7a7a;
    --mark: #bdbdbd;
    --icon: #5a5a5a;
    --photo-deep: #24170a;
    --photo-warm: #6b4a22;
    --photo-glow: #b38a4a;
  }
  * { margin: 0; padding: 0; box-sizing: border-box; }
  html, body { width: 1200px; height: 900px; overflow: hidden; background: var(--bg); }
  body { position: relative; font-family: "Jost", "Futura", sans-serif; font-weight: 300; color: var(--text-soft); }

  .brand { position: absolute; left: 118px; top: 18px; width: 220px; }
  .brand-mark { position: absolute; left: 45px; top: 0; width: 100px; height: 100px; border-radius: 50%; background: var(--mark); }
  .brand-name { position: absolute; left: 0; top: 118px; font-size: 45px; line-height: 1; color: var(--text-mute); font-weight: 300; white-space: nowrap; letter-spacing: 0.3px; }
  .brand-sub { position: absolute; left: 20px; top: 170px; font-size: 13px; letter-spacing: 6.6px; color: var(--text-mute); font-weight: 300; white-space: nowrap; }

  .main-nav { position: absolute; left: 330px; top: 48px; width: 750px; height: 22px; border-bottom: 1px solid var(--rule-light); }
  .main-nav ul { list-style: none; display: flex; }
  .main-nav li { font-size: 13px; letter-spacing: 0.2px; color: var(--text-soft); text-transform: uppercase; position: relative; height: 21px; white-space: nowrap; }
  .main-nav li.is-active { color: var(--text-bright); }
  .main-nav li.is-active::after { content: ""; position: absolute; left: 0; right: 0; bottom: -1px; border-bottom: 1px solid var(--text-bright); }
  .nav-home { padding: 0 8px; width: 54px; }
  .nav-about { margin-left: 20px; width: 73px; }
  .nav-portfolio { margin-left: 19px; width: 78px; }
  .nav-gallery { margin-left: 19px; width: 55px; }
  .nav-investment { margin-left: 19px; width: 79px; }
  .nav-contact { margin-left: 18px; }

  .social-links { position: absolute; left: 925px; top: 46px; display: flex; gap: 19px; }
  .social-links span { width: 16px; height: 16px; border-radius: 50%; background: var(--icon); display: block; }

  .hero-photo { position: absolute; left: 727px; top: 130px; width: 473px; height: 720px;
    background:
      linear-gradient(to right, var(--bg) 0%, rgba(0,0,0,0.55) 18%, rgba(0,0,0,0) 40%),
      radial-gradient(ellipse 34% 58% at 62% 58%, var(--photo-glow) 0%, var(--photo-warm) 55%, rgba(36,23,10,0) 100%),
      linear-gradient(to bottom, var(--photo-deep) 0%, #150d05 100%); }

  .hero-copy { position: absolute; left: 118px; top: 385px; width: 486px; }
  .hero-title { display: inline-block; font-size: 37px; font-weight: 300; letter-spacing: 1.4px; color: var(--text-soft); padding: 0 8px 2px 7px; border-bottom: 1px solid var(--rule-light); line-height: 44px; }
  .hero-text { margin-top: 12px; font-size: 12.4px; letter-spacing: 0.2px; text-transform: uppercase; color: var(--text-soft); white-space: nowrap; }
  .hero-link { display: block; margin-top: 14px; text-align: right; font-size: 13px; letter-spacing: 0.4px; color: var(--text-bright); padding-right: 2px; }

  .site-footer { position: absolute; left: 120px; top: 839px; width: 960px; border-top: 1px solid var(--rule); text-align: center; padding-top: 10px; font-size: 10.5px; letter-spacing: 0.5px; color: var(--text-mute); }
</style>
</head>
<body>
  <header>
    <div class="brand">
      <span class="brand-mark"></span>
      <div class="brand-name">selka varon</div>
      <div class="brand-sub">PHOTOGRAPHY</div>
    </div>
    <nav class="main-nav">
      <ul>
        <li class="nav-home is-active">Home</li>
        <li class="nav-about">About Me</li>
        <li class="nav-portfolio">Portfolio</li>
        <li class="nav-gallery">Gallery</li>
        <li class="nav-investment">Investment</li>
        <li class="nav-contact">Contact</li>
      </ul>
    </nav>
    <div class="social-links" aria-label="Social media links">
      <span></span><span></span><span></span><span></span><span></span>
    </div>
  </header>

  <main>
    <div class="hero-photo" role="img" aria-label="Portrait of a woman in a long golden satin dress with a red flower crown, seated against a dark background"></div>
    <section class="hero-copy">
      <h1 class="hero-title">CLASS ELEGANCE</h1>
      <p class="hero-text">Lorem ipsum dolor sit amet, consectetur adipiscing elit. Ut lobortis leo et</p>
      <a class="hero-link">LEARN MORE</a>
    </section>
  </main>

  <footer class="site-footer">COPYRIGHT © 2015 SELKA VARON PHOTOGRAPHY</footer>
</body>
</html>
```